Antibacterial Hand Wash Squeeze Tube Label

We're looking for a contemporary label design for a new Antibacterial Hand Wash for an 8oz squeeze tube. The new consumer brand will be sold to consumers in major US retail stores & online. The moisturizing hand wash contains Aloe Vera, vitamin E, and other natural ingredients so the design should include the color green. Real photos are very effective on packaging, so a picture of Aloe Vera or possibly two hands washing would help draw consumers' attention to the tube on the retail shelf. The front label may wrap around the sides. Rear must be left mostly blank
US Consumers - retail stores & online
Consumer

```html
<!DOCTYPE html>
<html lang="en">
<head>
<meta charset="utf-8">
<title>Moisturizing Hand Wash – Tube Label Dieline</title>
<link rel="stylesheet" href="https://fonts.googleapis.com/css2?family=Open+Sans:wght@400;600;700&display=swap">
<style>
  :root {
    --page-bg: #e4e4e4;
    --dieline-fill: #ffffff;
    --dieline-stroke: #1a1a1a;
    --green-deep: #2f7a12;
    --green-mid: #4e9e1f;
    --green-bright: #7ccc2c;
    --green-banner: #3a8516;
    --text-light: #ffffff;
    --skin-light: #e9c9b3;
    --aloe-soft: #6fb63a;
  }
  html, body {
    margin: 0;
    padding: 0;
    width: 1200px;
    height: 1200px;
    overflow: hidden;
    background: var(--page-bg);
  }
  .canvas {
    position: relative;
    width: 1200px;
    height: 1200px;
  }
  .tube-dieline {
    position: absolute;
    left: 175px;
    top: 69px;
    width: 852px;
    height: 1064px;
  }
  .label-text {
    font-family: "Open Sans", sans-serif;
    fill: var(--text-light);
    text-anchor: middle;
  }
  .title-line { font-weight: 700; }
  .claim-line { font-weight: 600; font-size: 26px; }
  .volume-line { font-weight: 400; font-size: 28px; }
  .origin-line { font-weight: 400; font-size: 16px; }
</style>
</head>
<body>
<main class="canvas">
  <svg class="tube-dieline" viewBox="0 0 852 1064" xmlns="http://www.w3.org/2000/svg">
    <defs>
      <linearGradient id="front-panel-gradient" x1="0" y1="0" x2="1" y2="1">
        <stop offset="0" stop-color="var(--green-mid)"/>
        <stop offset="0.45" stop-color="var(--green-bright)"/>
        <stop offset="0.7" stop-color="var(--green-mid)"/>
        <stop offset="1" stop-color="var(--green-deep)"/>
      </linearGradient>
      <linearGradient id="aloe-area-gradient" x1="0" y1="1" x2="1" y2="0">
        <stop offset="0" stop-color="var(--aloe-soft)" stop-opacity="0.55"/>
        <stop offset="1" stop-color="var(--green-mid)" stop-opacity="0.35"/>
      </linearGradient>
      <linearGradient id="hands-area-gradient" x1="0" y1="0" x2="1" y2="0">
        <stop offset="0" stop-color="var(--skin-light)" stop-opacity="0.45"/>
        <stop offset="1" stop-color="var(--skin-light)" stop-opacity="0.2"/>
      </linearGradient>
      <clipPath id="front-panel-clip">
        <rect x="424.5" y="79.5" width="426" height="843"/>
      </clipPath>
    </defs>

    <g class="dieline" fill="none" stroke="var(--dieline-stroke)" stroke-width="1">
      <rect class="tube-body" x="0.5" y="0.5" width="851" height="958" fill="var(--dieline-fill)"/>
      <line class="crimp-line" x1="0" y1="36.5" x2="852" y2="36.5"/>
      <line class="crimp-line" x1="0" y1="71.5" x2="852" y2="71.5"/>
      <line class="crimp-line" x1="0" y1="79.5" x2="852" y2="79.5"/>
      <line class="shoulder-line" x1="0" y1="922.5" x2="852" y2="922.5"/>
      <line class="back-front-fold" x1="424.5" y1="79.5" x2="424.5" y2="922.5"/>
      <polyline class="tube-shoulder" points="426,958.5 576.5,1020.5 702.5,1020.5 851,958.5" fill="var(--dieline-fill)"/>
      <rect class="nozzle" x="576.5" y="1020.5" width="126" height="42" fill="var(--dieline-fill)"/>
      <line x1="576.5" y1="1028.5" x2="702.5" y2="1028.5"/>
      <line x1="576.5" y1="1036.5" x2="702.5" y2="1036.5"/>
      <line x1="576.5" y1="1044.5" x2="702.5" y2="1044.5"/>
      <line x1="576.5" y1="1052.5" x2="702.5" y2="1052.5"/>
    </g>

    <g class="front-panel" clip-path="url(#front-panel-clip)">
      <rect class="front-panel-bg" x="424.5" y="79.5" width="426" height="843" fill="url(#front-panel-gradient)"/>

      <rect class="title-banner" x="498" y="154" width="278" height="97" fill="var(--green-banner)"/>
      <path class="title-banner-curve" d="M498 251 Q 637 275 776 251" fill="none" stroke="var(--green-bright)" stroke-width="3"/>
      <text class="label-text title-line" x="638" y="192" font-size="31">MOISTURIZING</text>
      <text class="label-text title-line" x="638" y="230" font-size="37">HAND WASH</text>

      <text class="label-text claim-line" x="638" y="317">Contains Aloe Vera</text>
      <text class="label-text claim-line" x="638" y="350">Vitamin E</text>

      <rect class="aloe-photo" role="img" aria-label="Photo of a cut aloe vera leaf dripping gel"
            x="586" y="381" width="207" height="150" rx="12" fill="url(#aloe-area-gradient)"/>

      <rect class="hands-photo" role="img" aria-label="Photo of two cupped hands held out to catch the gel"
            x="424" y="540" width="368" height="160" rx="12" fill="url(#hands-area-gradient)"/>

      <path class="shield-icon" d="M638 721 Q 660 732 682 732 L 682 765 Q 680 790 638 802 Q 596 790 594 765 L 594 732 Q 616 732 638 721 Z"
            fill="var(--green-deep)" stroke="var(--green-bright)" stroke-width="2"/>
      <path class="shield-plus" d="M632 746 h12 v12 h12 v12 h-12 v12 h-12 v-12 h-12 v-12 h12 Z"
            fill="none" stroke="var(--text-light)" stroke-width="1.5"/>

      <text class="label-text volume-line" x="638" y="841">8 FL OZ (200mL)</text>
      <text class="label-text origin-line" x="638" y="886">MADE IN USA</text>
    </g>
  </svg>
</main>
</body>
</html>
```